School Canteen Menu

We operate 30 school canteen/cafes across Melbourne. We are looking to update our old menu to a new attractive design.
We offer a variety of both food and drink and we need to highlight our healthy options. We would like to have a background picture of either salads or healthy sandwiche etc.
We have borken our current menu in catogories according to hot food, cold bar, drinks, ice creams etc.
We would prefer it to be a A4 design but other ideas are welcome.

In summary we need a vibrant attractive applealing design.
My business card with our lgo is also attached
Regards

Tam
Updates

We have two types of menu a secondary menu for students 12-18 and a primary school menu 5-12 year olds. I have attached samples of both.

Reason: Extended deadline as the director of business is away till sunday

Target Market(s)

12 year old to 18 year olds. School Students. As well as Teachers. Prehaps encouraging Teaches with our Freshly made salads will be a feature.

Industry/Entity Type

School

Requirements
Must have
• Viabrant Colors. Greens, Purples, Yellows.
Should not have
• Red Colors. Considered to be a unhealthy color.

```html
<!DOCTYPE html>
<html lang="en">
<head>
<meta charset="utf-8">
<title>Canteen Menu 2012</title>
<link href="https://fonts.googleapis.com/css2?family=Arimo:ital,wght@0,400;0,700;1,700&display=swap" rel="stylesheet">
<style>
:root{
  --purple:#7a2b8c;
  --purple-dark:#5e1d6e;
  --purple-light:#9b46ad;
  --green:#3d9a2a;
  --ink:#3a2f2a;
  --paper:#ffffff;
}
*{margin:0;padding:0;box-sizing:border-box}
html,body{width:849px;height:1200px;overflow:hidden;background:var(--paper)}
body{font-family:"Arimo",Arial,sans-serif;color:var(--ink);position:relative}
.masthead{position:absolute;left:0;top:0;width:849px;height:88px;
  background:linear-gradient(180deg,var(--purple-light),var(--purple) 60%,var(--purple-dark));
  display:flex;align-items:center;justify-content:center}
.masthead h1{color:#fff;font-size:38px;font-weight:700;letter-spacing:.5px}
.backdrop{position:absolute;left:0;top:88px;width:849px;height:1072px;
  background:
    radial-gradient(ellipse 300px 260px at 300px 600px,rgba(214,72,40,.6),transparent 70%),
    radial-gradient(ellipse 340px 300px at 540px 520px,rgba(110,185,50,.6),transparent 70%),
    radial-gradient(ellipse 260px 220px at 470px 760px,rgba(240,190,60,.5),transparent 70%),
    radial-gradient(ellipse 600px 560px at 420px 600px,rgba(180,215,140,.55),transparent 75%),
    #fff}
.veil{position:absolute;left:0;top:88px;width:849px;height:1072px;background:rgba(255,255,255,.5)}
.column{position:absolute;top:102px;display:flex;flex-direction:column;justify-content:space-between}
.column.left{left:38px;width:370px;height:1000px}
.column.right{left:444px;width:370px;height:1046px}
.bar{background:linear-gradient(180deg,var(--purple-light),var(--purple));color:#fff;
  font-weight:700;font-size:15px;text-transform:uppercase;height:26px;line-height:26px;padding-left:8px;margin-bottom:5px}
.sub{color:var(--green);font-weight:700;font-style:italic;font-size:15px;line-height:20px;margin:2px 0 2px}
.item{display:grid;grid-template-columns:1fr 58px;font-size:14.5px;line-height:19px;margin-bottom:3px}
.item .price{text-align:right}
.sub.item .price{color:var(--ink);font-style:normal;font-weight:400}
.note{font-size:14.5px;line-height:19px;margin-bottom:4px}
.footer{position:absolute;left:0;bottom:0;width:849px;height:40px;
  background:linear-gradient(180deg,var(--purple),var(--purple-dark));color:#fff;
  font-size:16px;font-weight:700;display:flex;align-items:center;justify-content:center;gap:14px}
</style>
</head>
<body>
<header class="masthead"><h1>Canteen Menu 2012</h1></header>
<div class="backdrop" role="img" aria-label="Background photograph of a fresh green salad with tomatoes and capsicum"></div>
<div class="veil"></div>

<main>
<div class="column left">
  <section class="section">
    <div class="bar">Hot Food</div>
    <div class="sub">Jaffles</div>
    <div class="item"><span>Cheese</span><span class="price">$2.50</span></div>
    <div class="item"><span>Spaghetti</span><span class="price">$2.50</span></div>
    <div class="item"><span>Baked Beans</span><span class="price">$2.50</span></div>
    <div class="item"><span>Ham &amp; Cheese</span><span class="price">$2.60</span></div>
    <div class="item"><span>Ham, Cheese &amp; Pineapple</span><span class="price">$3.00</span></div>
    <div class="item"><span>Lasagne 97% Fat Free</span><span class="price">$3.60</span></div>
    <div class="item"><span>Macaroni &amp; Cheese 97% Fat Free</span><span class="price">$3.60</span></div>
    <div class="item"><span>Meat Pie</span><span class="price">$3.20</span></div>
    <div class="item"><span>Party Pie or Party Sausage Roll</span><span class="price">$1.00</span></div>
    <div class="item"><span>Sausage Roll</span><span class="price">$3.00</span></div>
    <div class="item"><span>Flame Grilled Beef Burger with lettuce, cheese and tomato</span><span class="price">$4.00</span></div>
    <div class="item"><span>Chicken Burger with lettuce, cheese &amp; mayonnaise</span><span class="price">$4.00</span></div>
    <div class="item"><span>Baked Chicken Schnitzel Roll with lettuce, cheese, tomato &amp; mayo</span><span class="price">$4.20</span></div>
    <div class="item"><span>Corn Cobette</span><span class="price">$1.20</span></div>
    <div class="item"><span>Noodles - Chicken or Beef</span><span class="price">$1.50</span></div>
    <div class="item"><span>Chicken Nuggets 60c each (3)</span><span class="price">$2.00</span></div>
    <div class="item"><span>Steamed Dim Sim</span><span class="price">$0.50</span></div>
    <div class="item"><span>Hot Dog</span><span class="price">$3.00</span></div>
  </section>

  <section class="section">
    <div class="bar">Specials</div>
    <div class="item sub"><span>Health Pack 1</span><span class="price">$6.00</span></div>
    <div class="note">Salad Roll, Cookie &amp; 200ml Fruit Box</div>
    <div class="item sub"><span>Health Pack 2</span><span class="price">$6.00</span></div>
    <div class="note">Any 97% Fat Free Pasta, 300ml Flavoured Milk(FRESH)</div>
  </section>

  <section class="section">
    <div class="bar">Salad Plates</div>
    <div class="note">Salad Plates<br>all with lettuce, cucumber, carrot, tomato &amp; beetroot</div>
    <div class="item"><span>Salad</span><span class="price">$3.40</span></div>
    <div class="item"><span>Egg</span><span class="price">$3.60</span></div>
    <div class="item"><span>Chicken</span><span class="price">$3.90</span></div>
    <div class="item"><span>Cheese</span><span class="price">$3.60</span></div>
    <div class="item"><span>Ham</span><span class="price">$3.60</span></div>
    <div class="item"><span>Tuna</span><span class="price">$3.60</span></div>
  </section>
</div>

<div class="column right">
  <section class="section">
    <div class="bar">Sandwiches</div>
    <div class="sub">Sandwiches Rolls 60c extra</div>
    <div class="item"><span>Salad &nbsp;lettuce, tomato, carrot, beetroot, cucumber</span><span class="price">$2.80</span></div>
    <div class="item"><span>Ham &amp; Tomato</span><span class="price">$2.80</span></div>
    <div class="item"><span>Ham, Cheese &amp; Tomato</span><span class="price">$2.60</span></div>
    <div class="item"><span>Cheese &amp; Tomato</span><span class="price">$2.60</span></div>
    <div class="item"><span>Cheese &amp; Salad</span><span class="price">$3.00</span></div>
    <div class="item"><span>Egg &amp; Lettuce</span><span class="price">$2.80</span></div>
    <div class="item"><span>Chicken &amp; Salad</span><span class="price">$3.10</span></div>
    <div class="item"><span>Tuna &amp; Tomato</span><span class="price">$2.90</span></div>
    <div class="item"><span>Tuna, Lettuce &amp; Mayonnaise</span><span class="price">$3.00</span></div>
    <div class="item"><span>Savoury Spread</span><span class="price">$1.60</span></div>
    <div class="item"><span>Ham</span><span class="price">$2.20</span></div>
    <div class="item"><span>extra fillings</span><span class="price">$0.40</span></div>
  </section>

  <section class="section">
    <div class="bar">Wraps</div>
    <div class="sub">BBQ Chicken</div>
    <div class="item"><span>Chicken, Lettuce, BBQ Sauce</span><span class="price">$3.60</span></div>
    <div class="sub">Sweet Chili Chicken</div>
    <div class="item"><span>Chicken, Lettuce, Sweet Chilli Sauce</span><span class="price">$3.60</span></div>
  </section>

  <section class="section">
    <div class="bar">Snacks</div>
    <div class="item"><span>Pikelets</span><span class="price">$0.80</span></div>
    <div class="item"><span>Pop Corn</span><span class="price">$2.00</span></div>
    <div class="item"><span>Fruit Salad - small</span><span class="price">$1.50</span></div>
    <div class="item"><span>Fruit of the day</span><span class="price">$0.80</span></div>
    <div class="item"><span>Jelly Cup with Fruit</span><span class="price">$1.50</span></div>
    <div class="item"><span>Anzac Cookie</span><span class="price">$0.80</span></div>
    <div class="item"><span>Mini Muffins (home baked)</span><span class="price">$0.80</span></div>
  </section>

  <section class="section">
    <div class="bar">Drinks</div>
    <div class="item"><span>Flavoured Milk (300ml) Chocolate, Strawberry, Iced Coffee (FRESH)</span><span class="price">$2.50</span></div>
    <div class="item"><span>Water (600ml)</span><span class="price">$2.30</span></div>
    <div class="item"><span>Fruit Juice (300ml) Tropical, Orange, Apple</span><span class="price">$1.5</span></div>
  </section>

  <section class="section">
    <div class="bar">Ice Creams</div>
    <div class="item"><span>Frozen Orange Wedge</span><span class="price">$0.20</span></div>
    <div class="item"><span>Frozen Pineapple Ring</span><span class="price">$0.20</span></div>
    <div class="item"><span>Frozen Fruit Yoghurt</span><span class="price">$1.20</span></div>
    <div class="item"><span>Icy Tube</span><span class="price">$0.80</span></div>
    <div class="item"><span>Frosty Pop Orange, Lemonade</span><span class="price">$0.20</span></div>
  </section>
</div>
</main>

<footer class="footer"><span>freshbitecanteens.com.au</span><span>|</span><span>P.O Box 48 Northcote, VIC 3070</span></footer>
</body>
</html>
```